Darrow Kettle Lawyers needs a web design

We need a web design for our conveyancing and commercial law firm based in Sydney Australia. We want to depersonalise the current website: http://www.darrowkettle-example.com/ and give it a classic modern feel to it. It should be a simple design (possibly one page) and communicate trust, professionalism and experience.

Content should include:

Darrow Kettle is a boutique Sydney based legal practice specialising in business and property law.

We pride ourselves on our proactive, receptive and dynamic approach to client service. Our business survives on referrals from satisfied clients and professionals who respect the way we do business.

Practice areas

Business law

We act on the sale and purchase of businesses. We assist clients with structuring their businesses, drafting shareholder agreements and buy-sell arrangements. We have acted on a multitude of other commercial matters including franchising, distribution, marketing and business services (with a particular focus in the advertising sector).

Property law

We act for developers, commercial property investors, landlords and tenants. We also handle residential conveyancing and deal with strata and company title matters.

Private Client

We draft wills and codicils on behalf of clients and can also assist with applications for probate should the need arise.

Contact Us

Darrow Kettle
Level 14, Marlow Spire
7 Brennock Plaza
Sydney, NSW 2000

t: +61 (0)2 9471 6023
f: +61 (0)2 8265 4790
e: enquiries@darrowkettle-example.com

Target Market(s)

Individuals and business who need legal advice in the area of property and commercial law

Industry/Entity Type

Legal

Number of Pages Required

1 page

Font styles to use
Sans Serif

Requirements
Must have
• Clear and concise content.
Nice to have
• Some images to break up the content.
Should not have
• Any offensive images tones or connotations.

```html
<!DOCTYPE html>
<html lang="en">
<head>
<meta charset="utf-8">
<title>Darrow Kettle Lawyers</title>
<link href="https://fonts.googleapis.com/css2?family=Bree+Serif&family=Open+Sans:ital,wght@0,400;0,600;1,400&display=swap" rel="stylesheet">
<style>
:root{
  --navy:#143a72;
  --ink:#2b2b2b;
  --muted:#7a7a7a;
  --panel:#f0f0f0;
  --line:#e2e2e2;
  --white:#ffffff;
  --dark:#3a3a3a;
}
*{box-sizing:border-box;margin:0;padding:0}
html,body{width:806px;height:1200px;overflow:hidden;background:var(--white)}
body{position:relative;font-family:'Open Sans',Arial,sans-serif;color:var(--ink)}
.serif{font-family:'Bree Serif',Georgia,serif}
.abs{position:absolute}

/* header */
.accent-strip{left:97px;top:0;width:183px;height:3px;background:var(--navy)}
.logo{left:105px;top:20px;font-family:'Open Sans',Arial,sans-serif;color:var(--navy)}
.logo .name{font-size:24px;line-height:28px;letter-spacing:-.3px}
.logo .sub{font-size:11px;text-align:right;line-height:12px}
.topbar{left:427px;top:0;width:291px;height:17px;background:var(--panel);font-size:7px;color:#333;display:flex;align-items:center;justify-content:flex-end;gap:14px;padding-right:18px}
.topbar span{display:flex;align-items:center;gap:5px}
.nav{left:357px;top:38px;display:flex;gap:0;font-family:'Bree Serif',Georgia,serif;font-size:12.5px;color:#555}
.nav a{text-decoration:none;color:#5a6270;margin-right:19px}
.nav a.active{color:var(--navy)}

/* hero */
.hero{left:0;top:80px;width:806px;height:289px;background:linear-gradient(90deg,#e6e6e6 0%,#f5f5f5 30%,#eaeaea 55%,#dcdcdc 100%)}
.hero-photo{left:359px;top:80px;width:447px;height:289px;background:radial-gradient(ellipse at 55% 55%,#b9bfcc 0%,#d8d6d2 45%,#e4e2df 100%)}
.kicker{left:125px;top:173px;font-size:12px;color:#333}
.headline{left:95px;top:170px;font-size:50px;color:#333;line-height:60px;letter-spacing:-.5px}
.kicker2{left:180px;top:218px;font-size:14px;color:#333}
.hero-copy{left:97px;top:244px;width:250px;font-size:8.2px;line-height:12.5px;color:#333}

/* features */
.band{left:0;top:369px;width:806px;height:104px;background:var(--navy);color:var(--white)}
.feature{position:absolute;top:22px;width:180px}
.feature h3{font-family:'Bree Serif',Georgia,serif;font-weight:400;font-size:14px;display:flex;align-items:center;gap:9px;height:18px}
.feature p{margin-top:11px;font-size:6.4px;line-height:11px}
.band-shadow{left:290px;top:473px;width:230px;height:12px;background:radial-gradient(ellipse at 50% 0,rgba(0,0,0,.14),rgba(0,0,0,0) 70%)}

/* team */
.member{position:absolute;top:504px;width:132px;text-align:center}
.portrait{width:132px;height:99px;background:linear-gradient(180deg,#eeeeee 0%,#c9c9c9 60%,#5a5a5a 100%);border:1px solid var(--line)}
.member h4{font-family:'Bree Serif',Georgia,serif;font-weight:400;font-size:11.5px;margin-top:9px;color:#222}
.member p{font-family:'Bree Serif',Georgia,serif;font-size:7.5px;margin-top:3px;color:#222}

/* services */
.service-list{left:96px;top:692px;width:131px;list-style:none;font-size:7.2px;color:#555}
.service-list li{height:22px;display:flex;align-items:center;gap:6px;padding-left:0}
.service-list li.current{background:var(--panel);border-top:2px solid var(--line);height:24px}
.service-list i{width:10px;height:10px;border-radius:50%;background:#2b2b2b;color:#fff;font-style:normal;font-size:9px;line-height:10px;text-align:center;display:inline-block}
.service-body{left:252px;top:692px;width:446px}
.service-body h2{font-family:'Bree Serif',Georgia,serif;font-weight:400;font-size:13.5px;color:#333}
.service-body p{font-size:7px;line-height:12.4px;color:var(--muted);margin-top:9px}
.service-body p+p{margin-top:12px}

/* testimonial */
.quote{left:96px;top:854px;width:602px;height:62px;background:#f3f3f3;border:1px solid var(--line);border-left:3px solid #444}
.avatar{position:absolute;left:19px;top:9px;width:40px;height:40px;border-radius:50%;background:radial-gradient(circle,#d9b99a 0%,#8aa0b5 100%);border:2px solid #fff}
.quote p{position:absolute;left:73px;top:11px;width:510px;font-size:8px;line-height:14.5px;font-style:italic;color:#666}
.quote .by{position:absolute;right:16px;top:43px;font-size:7.5px;font-style:italic;color:#444;display:flex;align-items:center;gap:5px}

/* footer */
.footer{left:0;top:948px;width:806px;height:217px;background:var(--panel)}
.footer h5{position:absolute;top:36px;font-family:'Bree Serif',Georgia,serif;font-weight:400;font-size:9.5px;text-transform:uppercase;color:#222}
.map{left:97px;top:1014px;width:199px;height:130px;background:linear-gradient(120deg,#efd98a 0%,#f3e6b8 55%,#a9cdf4 75%,#a9cdf4 100%);border:3px solid #fff;box-shadow:0 0 2px rgba(0,0,0,.2)}
.post{position:absolute;left:325px;width:240px;height:60px}
.thumb{position:absolute;left:0;top:0;width:56px;height:57px;border:2px solid #fff;box-shadow:0 0 2px rgba(0,0,0,.2)}
.post h6{position:absolute;left:67px;top:2px;font-family:'Bree Serif',Georgia,serif;font-weight:400;font-size:9.5px;color:#222}
.post p{position:absolute;left:67px;top:17px;width:160px;font-size:6px;line-height:9.8px;color:#666}
.field{position:absolute;left:581px;width:118px;background:#fff;border:1px solid #e8e8e8;font-size:6.5px;font-style:italic;color:#aaa;padding:5px 6px}
.send{left:640px;top:1126px;width:59px;height:18px;background:var(--dark);color:#fff;font-size:7.5px;display:flex;align-items:center;justify-content:center}
.copyright{left:97px;top:1177px;font-size:7px;color:#333}
</style>
</head>
<body>

<div class="abs accent-strip"></div>
<div class="abs logo">
  <div class="name">Darrow Kettle</div>
  <div class="sub">Lawyers</div>
</div>
<div class="abs topbar">
  <span><svg width="8" height="6" viewBox="0 0 8 6"><rect x=".5" y=".5" width="7" height="5" fill="none" stroke="#333"/><path d="M.5 .5 4 3.5 7.5 .5" fill="none" stroke="#333"/></svg>enquiries@darrowkettle-example.com</span>
  <span><svg width="7" height="7" viewBox="0 0 10 10"><path d="M2 0 4 3 3 4Q4 6 6 7L7 6 10 8 8 10Q0 9 0 2Z" fill="#333"/></svg>(02) 9471 6023</span>
</div>
<nav class="abs nav">
  <a class="active" href="#">Home</a>
  <a href="#">Our Profile</a>
  <a href="#">Practice Areas</a>
  <a href="#">Testimonials</a>
  <a href="#" style="margin-right:0">Contact</a>
</nav>

<div class="abs hero"></div>
<div class="abs hero-photo" role="img" aria-label="Photo of two smiling lawyers in business suits"></div>
<div class="abs kicker serif">Stay Responsive</div>
<div class="abs headline serif">Anywhere</div>
<div class="abs kicker2 serif">You Are...</div>
<p class="abs hero-copy">Lorem ipsum dolor sit amet, consectetur adipisicing elit, sed do eiusmod tempor incididunt..</p>

<section class="abs band">
  <div class="feature" style="left:96px">
    <h3><svg width="20" height="16" viewBox="0 0 20 16"><rect x="0" y="3" width="20" height="13" rx="2" fill="#fff"/><rect x="7" y="0" width="6" height="4" rx="1" fill="none" stroke="#fff" stroke-width="1.6"/><rect x="0" y="8" width="20" height="1.2" fill="#143a72"/></svg>Solid Law Practice</h3>
    <p>Lorem ipsum dolor sit amet, consectetur adipisicing elit, sed do eiusmod tempor incididunt ut labore et dolore magna aliqua.</p>
  </div>
  <div class="feature" style="left:296px">
    <h3><svg width="14" height="18" viewBox="0 0 14 18"><path d="M7 1A6 6 0 0 0 3 11V14H11V11A6 6 0 0 0 7 1Z" fill="none" stroke="#fff" stroke-width="1.6"/><rect x="4" y="15.5" width="6" height="2" fill="#fff"/></svg>Creative Thinking</h3>
    <p>Lorem ipsum dolor sit amet, consectetur adipisicing elit, sed do eiusmod tempor incididunt ut labore et dolore magna aliqua.</p>
  </div>
  <div class="feature" style="left:497px">
    <h3><svg width="18" height="17" viewBox="0 0 18 17"><path d="M4 1H14V6A5 5 0 0 1 4 6Z" fill="#fff"/><path d="M4 3H1Q1 8 5 8M14 3H17Q17 8 13 8" fill="none" stroke="#fff" stroke-width="1.4"/><rect x="8" y="10" width="2" height="4" fill="#fff"/><rect x="5" y="14" width="8" height="2.5" fill="#fff"/></svg>Award Winning Company</h3>
    <p>Lorem ipsum dolor sit amet, consectetur adipisicing elit, sed do eiusmod tempor incididunt ut labore et dolore magna aliqua.</p>
  </div>
</section>
<div class="abs band-shadow"></div>

<div class="member" style="left:96px"><div class="portrait" role="img" aria-label="Portrait of Owen Marsh"></div><h4>Owen Marsh</h4><p>Solicitor Director</p></div>
<div class="member" style="left:253px"><div class="portrait" role="img" aria-label="Portrait of Liam Fenwick"></div><h4>Liam Fenwick</h4><p>Consultant</p></div>
<div class="member" style="left:409px"><div class="portrait" role="img" aria-label="Portrait of Rhys Calder"></div><h4>Rhys Calder</h4><p>Consultant</p></div>
<div class="member" style="left:566px"><div class="portrait" role="img" aria-label="Portrait of Tessa Whitlow"></div><h4>Tessa Whitlow</h4><p>Licenced Conveyancer</p></div>

<ul class="abs service-list">
  <li class="current"><i>+</i>Business</li>
  <li><i>+</i>Litigation</li>
  <li><i>+</i>Family Matters</li>
  <li><i>+</i>Property</li>
</ul>
<div class="abs service-body">
  <h2>We can place a sub-heading here regarding this service</h2>
  <p>Lorem ipsum dolor sit amet, consectetur adipisicing elit, sed do eiusmod tempor incididunt ut labore et dolore magna aliqua. Ut enim ad minim veniam, quis nostrud exercitation ullamco laboris nisi ut aliquip ex ea commodo consequat. Duis aute irure dolor in reprehenderit in voluptate velit esse cillum dolore eu fugiat nulla pariatur. Excepteur sint occaecat cupidatat non proident, sunt in culpa qui officia deserunt mollit anim id est laborum.</p>
  <p>Duis aute irure dolor in reprehenderit in voluptate velit esse cillum dolore eu fugiat nulla pariatur. Excepteur sint occaecat cupidatat non proident, sunt in culpa qui officia deserunt mollit anim id est laborum.</p>
</div>

<div class="abs quote">
  <div class="avatar" role="img" aria-label="Client portrait"></div>
  <p>Darrow Kettle has provided us with excellent advice on a number of our contracts with key blue chip clients. They are committed to protecting our position and providing a+ service. We will continue to engage them as our preferred legal advisers.</p>
  <div class="by">by <span style="color:#222">Aaron Pell</span>
    <svg width="14" height="7" viewBox="0 0 14 7"><path d="M4 .5 1 3.5 4 6.5M10 .5 13 3.5 10 6.5" fill="none" stroke="#222" stroke-width="1.2"/></svg></div>
</div>

<footer class="abs footer">
  <h5 style="left:97px">Find our office</h5>
  <h5 style="left:325px">Advices &amp; best practices</h5>
  <h5 style="left:581px">Quick contact</h5>
</footer>
<div class="abs map" role="img" aria-label="Map showing the office location in Sydney"></div>

<div class="post" style="top:1014px">
  <div class="thumb" style="background:linear-gradient(160deg,#6f8a3c,#c9d7a0 60%,#4f6a2a)" role="img" aria-label="Photo of green plants"></div>
  <h6>Strategies for your Success</h6>
  <p>Lorem ipsum dolor sit amet, consectetur elit, sed do eiusmod tempor. Officia deserunt mollit anim id est laborum reprehenderit in voluptate sint occaecat cupidatat.</p>
</div>
<div class="post" style="top:1088px">
  <div class="thumb" style="background:linear-gradient(180deg,#9fc0de 0%,#5e8db4 45%,#c7b9a0 75%,#a89a82 100%)" role="img" aria-label="Photo of a beach"></div>
  <h6>Strategies for your Success</h6>
  <p>Lorem ipsum dolor sit amet, consectetur elit, sed do eiusmod tempor. Officia deserunt mollit anim id est laborum reprehenderit in voluptate sint occaecat cupidatat.</p>
</div>

<div class="field" style="top:1012px;height:18px">Email</div>
<div class="field" style="top:1038px;height:18px">Subject</div>
<div class="field" style="top:1064px;height:48px">Text</div>
<div class="abs send">Send</div>

<div class="abs copyright">Copyright © 2015 Darrow Kettle, All rights reserved.</div>

</body>
</html>
```